New business logo / Business Card Design

My company provides Interim Management and consultancy, for Facilities Services. Covers any aspect of facilities management, including M&E, helpdesk, asset management, supplier relationships, catering, cleaning etc. Company provides innovative solutions to exceed client needs, drawing on years of experience. Initial thoughts on logo are attached below. Fits with RAG status on projects, red, amber and green, with logo design colours around moving services from amber to green.

Target Market(s)

Facilities Management clients and service providers

Industry/Entity Type

Business

Contact Information for Business Card

Company Name = k7Rventures Ltd My name on card = Derek Whitcombe, Director Mobile = 07516309842 Email = Derek@k7rventuresltd.co.uk Twitter = @k7Rventures Ltd

Font styles to use
Sans Serif

Colors
f37122
00a990

Requirements
Must have
• Logo to be evident, with some background image in reference to Facilities Management

```html
<!DOCTYPE html>
<html lang="en">
<head>
<meta charset="utf-8">
<title>k7Rventures Ltd – Business Card</title>
<link rel="stylesheet" href="https://fonts.googleapis.com/css2?family=Open+Sans:wght@400;600;700&display=swap">
<style>
  :root {
    --backdrop: #2b2b2b;
    --card: #1b1b1b;
    --amber: #f37122;
    --green: #00a990;
    --ink: #f2f2f2;
    --ink-soft: #d6d6d6;
  }
  * { margin: 0; padding: 0; box-sizing: border-box; }
  html, body {
    width: 1200px; height: 900px; overflow: hidden;
    background: var(--backdrop);
    font-family: "Open Sans", Arial, sans-serif;
  }
  .canvas {
    position: relative; width: 1200px; height: 900px;
  }
  .card {
    position: absolute; top: 300px;
    width: 500px; height: 300px;
    background: var(--card);
    border-radius: 20px;
  }
  .card--front { left: 70px; }
  .card--back { left: 630px; }

  .brand-mark {
    display: flex; flex-direction: column; align-items: center; gap: 14px;
    position: absolute;
  }
  .brand-circle {
    border-radius: 50%;
    background: var(--green);
  }
  .brand-name {
    color: var(--ink);
    font-weight: 700;
    white-space: nowrap;
  }

  .card--front .brand-mark { left: 40px; top: 75px; width: 180px; }
  .card--front .brand-circle { width: 120px; height: 120px; }
  .card--front .brand-name { font-size: 15px; }

  .card--back .brand-mark { left: 0; right: 0; top: 62px; }
  .card--back .brand-circle { width: 100px; height: 100px; }
  .card--back .brand-name { font-size: 30px; }

  .contact {
    position: absolute; left: 262px; top: 78px;
    color: var(--ink);
  }
  .contact__name {
    color: var(--amber); font-weight: 700; font-size: 18px; line-height: 1.2;
  }
  .contact__role {
    font-size: 13px; color: var(--ink-soft); margin-bottom: 16px;
  }
  .contact__list { list-style: none; }
  .contact__item {
    display: flex; align-items: center; gap: 10px;
    font-size: 13px; line-height: 1; margin-bottom: 9px;
  }
  .contact__icon { width: 12px; height: 12px; flex: none; }
  .contact__dot {
    width: 9px; height: 9px; border-radius: 50%;
    background: var(--amber); flex: none; margin: 0 1.5px;
  }
</style>
</head>
<body>
<main class="canvas">
  <section class="card card--front" aria-label="Business card front">
    <div class="brand-mark">
      <div class="brand-circle"></div>
      <div class="brand-name">k7Rventures Ltd</div>
    </div>
    <div class="contact">
      <p class="contact__name">Derek Whitcombe</p>
      <p class="contact__role">Director</p>
      <ul class="contact__list">
        <li class="contact__item">
          <svg class="contact__icon" viewBox="0 0 24 24" aria-hidden="true"><path fill="#f37122" d="M6.6 10.8a15 15 0 0 0 6.6 6.6l2.2-2.2a1 1 0 0 1 1-.25 11.4 11.4 0 0 0 3.6.57 1 1 0 0 1 1 1V20a1 1 0 0 1-1 1A17 17 0 0 1 3 4a1 1 0 0 1 1-1h3.5a1 1 0 0 1 1 1c0 1.25.2 2.45.57 3.57a1 1 0 0 1-.25 1z"/></svg>
          <span>07516309842</span>
        </li>
        <li class="contact__item">
          <svg class="contact__icon" viewBox="0 0 24 24" aria-hidden="true"><rect x="2" y="5" width="20" height="14" rx="2" fill="#f37122"/><path d="M3 6l9 7 9-7" fill="none" stroke="#1b1b1b" stroke-width="2"/></svg>
          <span>Derek@k7rventuresltd.co.uk</span>
        </li>
        <li class="contact__item">
          <span class="contact__dot"></span>
          <span>@k7Rventures Ltd</span>
        </li>
      </ul>
    </div>
  </section>

  <section class="card card--back" aria-label="Business card back">
    <div class="brand-mark">
      <div class="brand-circle"></div>
      <div class="brand-name">k7Rventures Ltd</div>
    </div>
  </section>
</main>
</body>
</html>
```